Fernhollow Estate Ventures Co.

We need a logo and business card design for a Hong Kong based real estate company, ORV Realty. We are want the brand to reflect the owners forward thinking, creative, and trend setting projects, while also reflecting a sense of security and strength. We invest in industrial properties which we convert to co-living or co-working spaces. ORV stands for Greater Bay Area which is the region around southern China including HK, Macau, and 9 other Chinese cities...made up of approx. 68 million people. There are massive infrastructure projects including the bridge to Macau and high-speed rail to SZ and the bridge connecting SZ and Zhongshan.

Target Market(s)

Chinese and western retail investors, as well as institutional investors

Industry/Entity Type

Real Estate Development

Contact Information for Business Card

Tomas Brennick
CEO
tomas@orvrealty.example
M + 852 9460 2157
F + 852 3582 0400
Suite 2207, Halvern Tower, 41 Marlow St., Central, Hong Kong

Logo Text

orv realty (company name) lifestyle property development (underneath)

Colors

Designer to choose colors to be used in the design.

Requirements
Must have
• Details listed above. One side should include the logo and company name...orv realty in modern, hip styling with "lifestyle property development"
Nice to have
• Could be a Black card, with metallic purple "orv" and white "land"...but open great design ideas
Should not have
• boring and traditional layout

```html
<!DOCTYPE html>
<html lang="en">
<head>
<meta charset="utf-8">
<title>ORV Realty – Business Card</title>
<link rel="stylesheet" href="https://fonts.googleapis.com/css2?family=Montserrat:wght@300;400&family=Saira:wght@500;700&display=swap">
<style>
  :root {
    --bg: #2b2f36;
    --card-black: #060606;
    --purple-deep: #5f2a92;
    --purple-light: #8a4fc0;
    --white: #ffffff;
    --cyan: #4cc3db;
    --rule: rgba(255,255,255,0.55);
  }
  * { margin: 0; padding: 0; box-sizing: border-box; }
  html, body {
    width: 1200px; height: 900px; overflow: hidden;
    background: var(--bg);
  }
  .stage {
    position: relative; width: 1200px; height: 900px;
    display: flex; flex-direction: column; align-items: center;
    justify-content: center; gap: 40px;
  }
  .card {
    position: relative; width: 700px; height: 400px;
    overflow: hidden;
    box-shadow: 0 14px 30px rgba(0,0,0,0.45);
  }
  /* Front */
  .card--front {
    background: var(--card-black);
    display: flex; flex-direction: column; align-items: center; justify-content: center;
  }
  .brand-name {
    font-family: "Saira", sans-serif; font-weight: 700;
    font-size: 96px; letter-spacing: 2px; line-height: 1;
    color: var(--white); text-transform: uppercase;
  }
  .brand-tagline {
    margin-top: 14px;
    font-family: "Saira", sans-serif; font-weight: 500;
    font-size: 19px; letter-spacing: 5px;
    color: var(--cyan); text-transform: uppercase;
  }
  /* Back */
  .card--back { color: var(--white); }
  .card-pattern {
    position: absolute; inset: 0;
    background: linear-gradient(160deg, var(--purple-light) 0%, var(--purple-deep) 100%);
  }
  .contact {
    position: relative; height: 100%;
    display: flex; flex-direction: column; align-items: center; justify-content: center;
    text-align: center; font-family: "Montserrat", sans-serif;
  }
  .contact-name {
    font-weight: 300; font-size: 38px; letter-spacing: 1px; text-transform: uppercase;
  }
  .contact-title { font-weight: 300; font-size: 20px; margin-top: 4px; }
  .divider { width: 220px; height: 1px; background: var(--rule); margin: 10px 0; }
  .dot { width: 6px; height: 6px; border-radius: 50%; background: var(--white); margin: 8px 0; }
  .contact-line { font-weight: 300; font-size: 15px; line-height: 1.55; }
</style>
</head>
<body>
  <main class="stage">
    <section class="card card--front" aria-label="Card front">
      <h1 class="brand-name">ORV Realty</h1>
      <p class="brand-tagline">Lifestyle Property Development</p>
    </section>

    <section class="card card--back" aria-label="Card back">
      <div class="card-pattern" role="img" aria-label="Faint repeating company name pattern on purple"></div>
      <div class="contact">
        <h2 class="contact-name">Tomas Brennick</h2>
        <div class="divider"></div>
        <p class="contact-title">CEO</p>
        <span class="dot"></span>
        <p class="contact-line">tomas@orvrealty.example</p>
        <div class="divider"></div>
        <p class="contact-line">M: + 852 9460 2157 | F: + 852 3582 0400</p>
        <span class="dot"></span>
        <p class="contact-line">Suite 2207, Halvern Tower, 41 Marlow St.</p>
        <p class="contact-line">Central, Hong Kong</p>
      </div>
    </section>
  </main>
</body>
</html>
```